Recruiting agency needs corporate presentation

We are a recruiting agency specialized in life sciences. We need a corporate presentation that will be sent to our clients and prospects in a PDF format.

Details of the presentation:
- a "brochure" type of presentation, VERTICAL, with 5 pages (please see "content" file attached) The presentation will be sent in a PDF format to our prospect clients by e-mail, so the choice of images and organization need to take that into account.
- In the attachment, you will find our logo "Keel & Associates".
- the presentation needs to convey our industry (life sciences, healthcare) and a high level of professionalism/leadership We want a sophisticated and elegant brochure.
- page 2 of the brochure needs to contain all the logos attached, in a very elegant, clear and organized way.
- page 3 shows a map with cursors (please see content file). The following countries/continents on the map need to be highlighted: USA, Brazil, Europe, North Africa, South Africa, China. We need "cursors" like pins to show where on the map our offices are: Miami, Boston, Lausanne, Denmark, Paris, Copenhaguen.
- page 4 includes pie charts (please see "Statistics 2020" Excel file): please improve the pie charts aesthetics, it needs to look very modern.

Healthcare / Life Sciences.

• Very modern and aesthetics. I included a presentation of companies that we like to give you an indication of the overall style we're looking for.

```html
<!DOCTYPE html>
<html lang="en">
<head>
<meta charset="utf-8">
<title>Keel &amp; Associates — Corporate Brochure</title>
<link href="https://fonts.googleapis.com/css2?family=Montserrat:wght@400;500;600;700&display=swap" rel="stylesheet">
<style>
:root{
  --bg:#d9dadc;
  --paper:#ffffff;
  --slate:#52658f;
  --gold:#c9a02f;
  --ink:#1f1f24;
  --muted:#555a66;
  --c-blue:#52658f;
  --c-teal:#45657a;
  --c-green:#3f7a5c;
  --c-olive:#8a8f43;
  --c-gold:#c5a233;
  --c-orange:#d1663f;
  --c-red:#d9404a;
  --c-mauve:#9b5a6e;
}
*{margin:0;padding:0;box-sizing:border-box}
html,body{width:1200px;height:1200px;overflow:hidden}
body{background:var(--bg);font-family:"Montserrat",sans-serif;color:var(--ink);position:relative}
.page{position:absolute;width:352px;height:456px;background:var(--paper);overflow:hidden}
.p-cover{left:211px;top:119px}
.p-clients{left:637px;top:119px}
.p-success{left:42px;top:625px}
.p-cover-stats{left:424px;top:625px}
.p-contact{left:806px;top:625px}
.abs{position:absolute}

.brand{position:absolute;text-align:left}
.brand-name{font-weight:700;font-size:8px;letter-spacing:1.6px;color:var(--ink);white-space:nowrap}
.brand-tag{font-weight:600;font-size:3.2px;letter-spacing:1.1px;color:var(--ink);margin-top:2px;white-space:nowrap}

.photo{position:absolute}
.photo-lab{background:linear-gradient(115deg,#cfcfcf 0%,#8d8d8d 35%,#e6e6e6 55%,#5a5a5a 100%)}
.photo-pipette{background:linear-gradient(160deg,#4a4a4a 0%,#bdbdbd 40%,#e9e9e9 60%,#6e6e6e 100%)}

.panel{position:absolute;background:var(--slate)}
.panel-lead{left:168px;top:146px;width:184px;height:163px}
.lead-caps{position:absolute;left:18px;top:37px;width:150px;font-size:4.4px;font-weight:600;letter-spacing:.9px;line-height:1.5;color:var(--gold);text-transform:uppercase}
.lead-rule{position:absolute;left:18px;top:86px;width:134px;height:.6px;background:#c4cad8}
.lead-body{position:absolute;left:18px;top:104px;width:146px;font-size:4.4px;letter-spacing:.6px;line-height:1.5;color:#fff}

.web{font-size:4.6px;font-weight:600;letter-spacing:1px;color:var(--gold);text-transform:uppercase}
.rule{position:absolute;height:.7px;background:#333}

.kicker{position:absolute;left:33px;top:45px;font-size:4.2px;font-weight:600;letter-spacing:.9px;color:var(--gold);text-transform:uppercase}
.title{position:absolute;left:32px;top:49px;font-size:17px;font-weight:400;color:var(--ink);letter-spacing:.2px}
.title-rule{position:absolute;left:33px;top:75px;width:286px;height:.7px;background:#333}
.footer{position:absolute;left:33px;top:428px;display:flex;align-items:center;width:286px}
.footer span{font-size:4.4px;font-weight:600;letter-spacing:1px;color:var(--gold);white-space:nowrap;margin-right:2px}
.footer i{flex:1;height:.6px;background:#333}

/* clients */
.p-clients .title-rule{width:235px}
.band-right{position:absolute;left:284px;top:0;width:68px;height:407px;background:var(--slate)}
.client-grid{position:absolute;left:33px;top:100px;display:grid;grid-template-columns:repeat(7,29px);grid-auto-rows:22px;column-gap:5px;row-gap:4px}
.client{background:#fff;box-shadow:0 0 0 .5px #d4d6db,0 1px 1.5px rgba(0,0,0,.18);display:flex;align-items:center;justify-content:center;text-align:center;font-size:3.6px;font-weight:600;color:var(--slate);line-height:1.1;padding:1px}
.client-note{grid-column:2 / span 5;display:flex;align-items:center;justify-content:center;text-align:center;font-size:4.4px;letter-spacing:.6px;line-height:1.4;color:var(--ink)}
.start-3{grid-column-start:3}

/* success */
.panel-map{left:0;top:97px;width:352px;height:309px}
.map-intro{position:absolute;left:34px;top:26px;width:285px;font-size:4.4px;letter-spacing:.5px;line-height:1.45;color:#fff}
.map-intro p+p{margin-top:5px}
.world-map{position:absolute;left:14px;top:91px;width:330px;height:168px;border-radius:6px;background:radial-gradient(ellipse at 30% 55%,rgba(201,160,47,.55) 0%,rgba(201,160,47,.18) 45%,rgba(82,101,143,0) 75%),radial-gradient(ellipse at 70% 40%,rgba(201,160,47,.45) 0%,rgba(82,101,143,0) 60%)}
.city{position:absolute;font-size:4.3px;font-weight:600;letter-spacing:.6px;color:#fff;white-space:nowrap}
.pin{position:absolute;width:7px;height:9px}

/* stats */
.stats-intro{position:absolute;left:34px;top:97px;width:285px;font-size:4.3px;letter-spacing:.5px;line-height:1.4;color:var(--ink)}
.donut{position:absolute;left:126px;width:100px;height:100px}
.d-label{position:absolute;font-size:4.3px;font-weight:600;letter-spacing:.3px;white-space:nowrap}
.d-left{right:238px;text-align:right}
.d-right{left:243px}
.lab-blue{color:var(--c-blue)}.lab-teal{color:var(--c-teal)}.lab-green{color:var(--c-green)}.lab-olive{color:var(--c-olive)}
.lab-gold{color:var(--c-gold)}.lab-orange{color:var(--c-orange)}.lab-red{color:var(--c-red)}.lab-mauve{color:var(--c-mauve)}

/* contact */
.band-left{position:absolute;left:0;top:0;width:168px;height:456px;background:var(--slate)}
.contact-block{position:absolute;left:33px;font-size:4.3px;letter-spacing:.4px;line-height:1.45;color:#fff}
.contact-block .gold{color:var(--gold)}
</style>
</head>
<body>

<!-- Page 1 : cover -->
<section class="page p-cover">
  <div class="brand" style="left:37px;top:58px">
    <div class="brand-name">KEEL &amp; ASSOCIATES</div>
    <div class="brand-tag">GLOBAL LIFE SCIENCES RECRUITING</div>
  </div>
  <div class="photo photo-lab" style="left:0;top:99px;width:352px;height:258px" role="img" aria-label="Black and white photo of a lab scientist in protective wear looking into a microscope"></div>
  <div class="panel panel-lead">
    <p class="lead-caps">We are an international recruiting boutique agency specialized in life sciences. In the last 3 decades, we have appointed thousands of professionals globally.</p>
    <div class="lead-rule"></div>
    <p class="lead-body">Our firm is known for being highly committed and able to deliver great results within budget and timing constraints. Equality and parity are at the core of our activity.</p>
  </div>
  <div class="abs web" style="left:34px;top:407px">www.keelassociates.com</div>
  <div class="rule" style="left:168px;top:410px;width:152px"></div>
</section>

<!-- Page 2 : clients -->
<section class="page p-clients">
  <div class="kicker">Our</div>
  <h2 class="title">Clients</h2>
  <div class="title-rule"></div>
  <div class="band-right"></div>
  <div class="client-grid">
    <div class="client">Brenqor</div><div class="client">Halvix Dx</div><div class="client">Orquell</div><div class="client">Imvoro</div><div class="client">Trixal</div><div class="client">Abbrel</div><div class="client">Felvanta</div>
    <div class="client">Aerquin</div><div class="client">Olcavi</div><div class="client">Axvenne</div><div class="client">Allumqa</div><div class="client">Arvezzo</div><div class="client">Orkavine</div><div class="client">Stelquor</div>
    <div class="client">Tidqua Bio</div><div class="client">Vatriq</div><div class="client">Bedrovo</div><div class="client">Besquen</div><div class="client">Bioqasta</div><div class="client">Biodrevo</div><div class="client">Garvanti</div>
    <div class="client">Bixomera</div><div class="client">Phyzolta</div><div class="client">Radqen Bio</div><div class="client">Simvarro</div><div class="client">Bledquo</div><div class="client">Carthovi</div><div class="client">Selqueno</div>
    <div class="client">Charvoss</div><div class="client">Quiesta</div><div class="client">Cytrovel</div><div class="client">Danquell</div><div class="client">Dervaxo</div><div class="client">Debrovin</div><div class="client">Diazomi</div>
    <div class="client">Lilvaro</div>
    <div class="client-note">Our clients range from innovative start-ups to<br>the largest global groups</div>
    <div class="client">Ferqani</div>
    <div class="client">Galdreva</div><div class="client">Gexalto</div><div class="client">Gekquor</div><div class="client">Genqira</div><div class="client">Zymqolt</div><div class="client">Gilvaro</div><div class="client">Bioqenta</div>
    <div class="client">Gaskova</div><div class="client">Guerlov</div><div class="client">Institut Varmel</div><div class="client">Ipsovra</div><div class="client">Alvequi</div><div class="client">Kelqora</div><div class="client">Leovanti</div>
    <div class="client">Macquova</div><div class="client">Magvrell</div><div class="client">Nexqolta</div><div class="client">Medvorin</div><div class="client">Merqova</div><div class="client">Nesqueta</div><div class="client">Brevfield Labs</div>
    <div class="client">Novarqi</div><div class="client">Nuxolva</div><div class="client">Oncovrel</div><div class="client">Polyqora</div><div class="client">Quintrevo</div><div class="client">Ferquol</div><div class="client">Heliqova</div>
    <div class="client">Rovanqi</div><div class="client">Takvero</div><div class="client">Theqova</div><div class="client">Tesqualo</div><div class="client">Totvaren</div><div class="client">Transqova</div><div class="client">Volqira</div>
    <div class="client start-3">Ypsqova</div><div class="client">Novalqir</div><div class="client">Theravquo</div>
  </div>
  <div class="footer"><span>KEEL &amp; ASSOCIATES (1)</span><i></i></div>
</section>

<!-- Page 3 : global success -->
<section class="page p-success">
  <div class="kicker">Our global</div>
  <h2 class="title">Success</h2>
  <div class="title-rule"></div>
  <div class="panel panel-map">
    <div class="map-intro">
      <p>Keel &amp; Associates's global success is driven by our multi-cultural team's ability to orchestrate an operational, innovative and direct approach to recruiting.</p>
      <p>Thanks to our global presence and proprietary offices in Europe and in the U.S., we have placed thousands of professionals in companies over 30 countries and 5 continents.</p>
    </div>
    <div class="world-map" role="img" aria-label="Outline world map with USA, Brazil, Europe, North Africa, South Africa and China highlighted in gold"></div>
  </div>
  <svg class="pin" style="left:96px;top:243px" viewBox="0 0 14 18"><path d="M7 17C7 17 1 10 1 6.5a6 6 0 0 1 12 0C13 10 7 17 7 17z" fill="#fff" stroke="#c8343f" stroke-width="1.6"/><circle cx="7" cy="6.5" r="2.2" fill="#c8343f"/></svg>
  <div class="city" style="left:104px;top:245px">Boston</div>
  <svg class="pin" style="left:88px;top:261px" viewBox="0 0 14 18"><path d="M7 17C7 17 1 10 1 6.5a6 6 0 0 1 12 0C13 10 7 17 7 17z" fill="#fff" stroke="#c8343f" stroke-width="1.6"/><circle cx="7" cy="6.5" r="2.2" fill="#c8343f"/></svg>
  <div class="city" style="left:97px;top:263px">Miami</div>
  <div class="city" style="left:142px;top:228px">Denmark</div>
  <svg class="pin" style="left:173px;top:227px" viewBox="0 0 14 18"><path d="M7 17C7 17 1 10 1 6.5a6 6 0 0 1 12 0C13 10 7 17 7 17z" fill="#fff" stroke="#c8343f" stroke-width="1.6"/><circle cx="7" cy="6.5" r="2.2" fill="#c8343f"/></svg>
  <div class="city" style="left:183px;top:230px">Copenhaguen</div>
  <div class="city" style="left:146px;top:237px">Paris</div>
  <svg class="pin" style="left:164px;top:235px" viewBox="0 0 14 18"><path d="M7 17C7 17 1 10 1 6.5a6 6 0 0 1 12 0C13 10 7 17 7 17z" fill="#fff" stroke="#c8343f" stroke-width="1.6"/><circle cx="7" cy="6.5" r="2.2" fill="#c8343f"/></svg>
  <svg class="pin" style="left:168px;top:241px" viewBox="0 0 14 18"><path d="M7 17C7 17 1 10 1 6.5a6 6 0 0 1 12 0C13 10 7 17 7 17z" fill="#fff" stroke="#c8343f" stroke-width="1.6"/><circle cx="7" cy="6.5" r="2.2" fill="#c8343f"/></svg>
  <div class="city" style="left:178px;top:242px">Lausanne</div>
  <div class="footer"><span>KEEL &amp; ASSOCIATES (2)</span><i></i></div>
</section>

<!-- Page 4 : what we cover -->
<section class="page p-cover-stats">
  <div class="kicker">What we</div>
  <h2 class="title">Cover</h2>
  <div class="title-rule"></div>
  <p class="stats-intro">We cover all sectors and all functions within Life Sciences. Each client is unique. Our solutions are tailor-made to your organization.</p>

  <svg class="donut" style="top:120px" viewBox="0 0 100 100" aria-label="Sectors chart">
    <g transform="rotate(-90 50 50)" fill="none" stroke-width="20">
      <circle cx="50" cy="50" r="30" pathLength="100" stroke="var(--c-blue)" stroke-dasharray="30.4 69.6" stroke-dashoffset="0"/>
      <circle cx="50" cy="50" r="30" pathLength="100" stroke="var(--c-teal)" stroke-dasharray="7.4 92.6" stroke-dashoffset="-31"/>
      <circle cx="50" cy="50" r="30" pathLength="100" stroke="var(--c-green)" stroke-dasharray="22.4 77.6" stroke-dashoffset="-39"/>
      <circle cx="50" cy="50" r="30" pathLength="100" stroke="var(--c-olive)" stroke-dasharray="8.4 91.6" stroke-dashoffset="-62"/>
      <circle cx="50" cy="50" r="30" pathLength="100" stroke="var(--c-gold)" stroke-dasharray="8.4 91.6" stroke-dashoffset="-71"/>
      <circle cx="50" cy="50" r="30" pathLength="100" stroke="var(--c-orange)" stroke-dasharray="2.4 97.6" stroke-dashoffset="-80"/>
      <circle cx="50" cy="50" r="30" pathLength="100" stroke="var(--c-red)" stroke-dasharray="2.4 97.6" stroke-dashoffset="-83"/>
      <circle cx="50" cy="50" r="30" pathLength="100" stroke="var(--c-mauve)" stroke-dasharray="13.4 86.6" stroke-dashoffset="-86"/>
    </g>
    <text x="50" y="52" text-anchor="middle" font-family="Montserrat,sans-serif" font-size="6.4" font-weight="700" letter-spacing=".4" fill="#1f1f24">SECTORS</text>
  </svg>
  <div class="d-label d-left lab-mauve" style="top:133px">Pharma 14% •</div>
  <div class="d-label d-left lab-red" style="top:151px">Hospital &amp; Clinics 3% •</div>
  <div class="d-label d-left lab-orange" style="top:169px">Animal Health 3% •</div>
  <div class="d-label d-left lab-gold" style="top:187px">Nutrition 9% •</div>
  <div class="d-label d-left lab-olive" style="top:205px">Digital Health 9% •</div>
  <div class="d-label d-right lab-blue" style="top:151px">• Biotech 31%</div>
  <div class="d-label d-right lab-teal" style="top:169px">• Medtech 8%</div>
  <div class="d-label d-right lab-green" style="top:187px">• Medical Device 23%</div>

  <svg class="donut" style="top:218px" viewBox="0 0 100 100" aria-label="Seniority chart">
    <g transform="rotate(-90 50 50)" fill="none" stroke-width="20">
      <circle cx="50" cy="50" r="30" pathLength="100" stroke="var(--c-blue)" stroke-dasharray="8.5 91.5" stroke-dashoffset="0"/>
      <circle cx="50" cy="50" r="30" pathLength="100" stroke="var(--c-teal)" stroke-dasharray="32.8 67.2" stroke-dashoffset="-9.1"/>
      <circle cx="50" cy="50" r="30" pathLength="100" stroke="var(--c-green)" stroke-dasharray="23 77" stroke-dashoffset="-42.5"/>
      <circle cx="50" cy="50" r="30" pathLength="100" stroke="var(--c-olive)" stroke-dasharray="33.3 66.7" stroke-dashoffset="-66.1"/>
    </g>
    <text x="50" y="52" text-anchor="middle" font-family="Montserrat,sans-serif" font-size="6.4" font-weight="700" letter-spacing=".4" fill="#1f1f24">SENIORITY</text>
  </svg>
  <div class="d-label d-left lab-olive" style="top:255px">Middle Management 33,9% •</div>
  <div class="d-label d-left lab-green" style="top:273px">Expert Management 23,6% •</div>
  <div class="d-label d-right lab-blue" style="top:255px">• Board Members 9,1%</div>
  <div class="d-label d-right lab-teal" style="top:273px">• Top Management 33,4%</div>

  <svg class="donut" style="top:316px" viewBox="0 0 100 100" aria-label="Function chart">
    <g transform="rotate(-90 50 50)" fill="none" stroke-width="20">
      <circle cx="50" cy="50" r="30" pathLength="100" stroke="var(--c-blue)" stroke-dasharray="6.2 93.8" stroke-dashoffset="0"/>
      <circle cx="50" cy="50" r="30" pathLength="100" stroke="var(--c-teal)" stroke-dasharray="3.6 96.4" stroke-dashoffset="-6.8"/>
      <circle cx="50" cy="50" r="30" pathLength="100" stroke="var(--c-green)" stroke-dasharray="26.9 73.1" stroke-dashoffset="-11"/>
      <circle cx="50" cy="50" r="30" pathLength="100" stroke="var(--c-olive)" stroke-dasharray="28.4 71.6" stroke-dashoffset="-38.5"/>
      <circle cx="50" cy="50" r="30" pathLength="100" stroke="var(--c-gold)" stroke-dasharray="3.6 96.4" stroke-dashoffset="-67.5"/>
      <circle cx="50" cy="50" r="30" pathLength="100" stroke="var(--c-orange)" stroke-dasharray="8.6 91.4" stroke-dashoffset="-71.7"/>
      <circle cx="50" cy="50" r="30" pathLength="100" stroke="var(--c-red)" stroke-dasharray="18.6 81.4" stroke-dashoffset="-80.9"/>
    </g>
    <text x="50" y="52" text-anchor="middle" font-family="Montserrat,sans-serif" font-size="6.4" font-weight="700" letter-spacing=".4" fill="#1f1f24">FUNCTION</text>
  </svg>
  <div class="d-label d-left lab-red" style="top:334px">R&amp;D 19,1% •</div>
  <div class="d-label d-left lab-orange" style="top:352px">Industrial 9,2% •</div>
  <div class="d-label d-left lab-gold" style="top:370px">HR 4,2% •</div>
  <div class="d-label d-left lab-olive" style="top:388px">Sales / Business Dev 29% •</div>
  <div class="d-label d-right lab-blue" style="top:343px">• Quality 6,8%</div>
  <div class="d-label d-right lab-teal" style="top:361px">• Finance/Legal 4,2%</div>
  <div class="d-label d-right lab-green" style="top:379px;line-height:1.4">• Medical/Reg./<br>&nbsp;&nbsp;Market Access 27,5%</div>

  <div class="footer"><span>KEEL &amp; ASSOCIATES (3)</span><i></i></div>
</section>

<!-- Page 5 : contact -->
<section class="page p-contact">
  <div class="band-left"></div>
  <div class="brand" style="left:224px;top:60px">
    <div class="brand-name">KEEL &amp; ASSOCIATES</div>
    <div class="brand-tag">GLOBAL LIFE SCIENCES RECRUITING</div>
  </div>
  <div class="photo photo-pipette" style="left:168px;top:99px;width:184px;height:258px" role="img" aria-label="Black and white photo of gloved hands using a pipette over test tubes"></div>
  <div class="contact-block" style="top:141px">
    <p class="gold">Thank you for your consideration.<br>We are looking forward to speaking with you.</p>
    <p style="margin-top:5px">recruitments@keelassociates.com<br>www.keelassociates.com</p>
  </div>
  <div class="contact-block" style="top:213px">
    <p class="gold">USA Headquarters</p>
    <p style="margin-top:5px">+1 (555) 014-2290<br>18 Harbor Lane<br>Boston, MA 02110</p>
  </div>
  <div class="contact-block" style="top:287px">
    <p class="gold">European Headquarters</p>
    <p style="margin-top:5px">+33 1 40 00 12 34<br>12 Rue des Lilas<br>Paris, France, 75008</p>
  </div>
  <div class="abs web" style="left:34px;top:407px">www.keelassociates.com</div>
</section>

</body>
</html>
```